KELVO Robotics Engineering Design Team - Pull Up Banner Design

I need a pull-up banner design which I can use at trade shows and events to market our research and development group. We are specialist design engineers who have expertise in:
- Embedded Electronics and Circuit Design
- Rapid Functional Prototyping
- Sensor and Vision Systems
- Robotics Systems

Recent projects include:
- Robotic concrete sewer probes
- IoT wildlife tracking systems
- Robots for exploring wombat burrows
- Smart pest control technology

Target Market(s)

Potential clients who want us to design a project for them

Industry/Entity Type

Engineering Consulting

Colors

Designer to choose colors to be used in the design.

Requirements
Must have
• Look professional and have a high-tech feel to it

```html
<!DOCTYPE html>
<html lang="en">
<head>
<meta charset="utf-8">
<title>KELVO Robotics – Pull Up Banner</title>
<link rel="stylesheet" href="https://fonts.googleapis.com/css2?family=Open+Sans:wght@300;400;600;700;800&display=swap">
<style>
  :root {
    --page-bg: #ececec;
    --brand-blue: #2b3d96;
    --blue-top: #2c3c9c;
    --blue-bottom: #172676;
    --red-top: #f5313f;
    --red-bottom: #c01a2a;
    --phone-red: #d3202f;
    --white: #ffffff;
    --grey-light: #fbfbfb;
    --grey-dark: #d4d4d4;
    --photo-sky: #8fb4df;
    --photo-mid: #8a7a5c;
    --photo-ground: #5f7a3a;
  }
  * { margin: 0; padding: 0; box-sizing: border-box; }
  html, body { width: 789px; height: 1200px; overflow: hidden; }
  body {
    background: var(--page-bg);
    font-family: "Open Sans", Arial, sans-serif;
    position: relative;
  }
  .banner {
    position: absolute;
    left: 144px;
    top: 25px;
    width: 501px;
    height: 1150px;
    background: var(--white);
    overflow: hidden;
    box-shadow: 0 4px 14px rgba(0,0,0,0.18);
  }
  .banner-shapes, .hero-photo {
    position: absolute;
    left: 0; top: 0;
    width: 501px; height: 1150px;
  }
  .brand-name {
    position: absolute;
    left: 0; width: 100%;
    top: 54px;
    text-align: center;
    font-size: 50px;
    font-weight: 800;
    letter-spacing: 10px;
    color: var(--brand-blue);
    line-height: 1;
  }
  .brand-services {
    position: absolute;
    left: 0; width: 100%;
    top: 125px;
    text-align: center;
    font-size: 13.5px;
    line-height: 20px;
    color: var(--brand-blue);
    letter-spacing: 0.3px;
  }
  .brand-url {
    position: absolute;
    left: 0; width: 100%;
    top: 165px;
    text-align: center;
    font-size: 19px;
    color: var(--brand-blue);
    line-height: 1;
  }
  .section-title {
    position: absolute;
    left: 55px;
    color: var(--white);
    font-size: 34px;
    line-height: 45px;
    text-transform: uppercase;
    white-space: nowrap;
  }
  .section-title .light { font-weight: 300; }
  .section-title .bold { font-weight: 800; }
  .expertise-title { top: 640px; }
  .projects-title { top: 881px; left: 52px; }
  .bullet-list {
    position: absolute;
    left: 58px;
    list-style: none;
    color: var(--white);
    font-size: 17.5px;
    font-weight: 700;
    line-height: 25.8px;
    white-space: nowrap;
  }
  .bullet-list li { position: relative; padding-left: 24px; }
  .bullet-list li::before {
    content: "";
    position: absolute;
    left: 4px; top: 9px;
    width: 9px; height: 9px;
    border-radius: 50%;
    background: var(--white);
    opacity: 0.85;
  }
  .expertise-list { top: 728px; }
  .projects-list { top: 929px; }
  .contact-phone {
    position: absolute;
    left: 0; width: 100%;
    top: 1087px;
    display: flex;
    justify-content: center;
    align-items: center;
    gap: 12px;
    color: var(--phone-red);
    font-size: 50px;
    font-weight: 800;
    line-height: 1;
    letter-spacing: -0.5px;
  }
  .phone-icon { width: 36px; height: 36px; }
</style>
</head>
<body>
  <div class="banner">
    <svg class="hero-photo" viewBox="0 0 501 1150" role="img"
         aria-label="Photo of the engineering team in high-visibility vests with a tripod-mounted sewer probe over a concrete manhole, work vehicles and stacked crates under a cloudy sky">
      <defs>
        <linearGradient id="photoTones" x1="0" y1="0" x2="0" y2="1">
          <stop offset="0" stop-color="var(--photo-sky)"/>
          <stop offset="0.45" stop-color="var(--photo-mid)"/>
          <stop offset="1" stop-color="var(--photo-ground)"/>
        </linearGradient>
      </defs>
      <polygon points="0,180 250,240 501,180 501,645 0,645" fill="url(#photoTones)"/>
    </svg>

    <svg class="banner-shapes" viewBox="0 0 501 1150" aria-hidden="true">
      <defs>
        <linearGradient id="redBand" x1="0" y1="0" x2="0" y2="1">
          <stop offset="0" stop-color="var(--red-top)"/>
          <stop offset="1" stop-color="var(--red-bottom)"/>
        </linearGradient>
        <linearGradient id="blueBand" x1="0" y1="0" x2="0" y2="1">
          <stop offset="0" stop-color="var(--blue-top)"/>
          <stop offset="1" stop-color="var(--blue-bottom)"/>
        </linearGradient>
        <linearGradient id="greyBand" x1="0" y1="0" x2="0" y2="1">
          <stop offset="0" stop-color="var(--grey-light)"/>
          <stop offset="1" stop-color="var(--grey-dark)"/>
        </linearGradient>
      </defs>
      <rect x="0" y="1060" width="501" height="90" fill="url(#greyBand)"/>
      <rect x="0" y="859" width="501" height="208" fill="url(#blueBand)"/>
      <polygon points="235,1066 266,1066 250.5,1084" fill="var(--blue-bottom)"/>
      <polygon points="0,637 250,572 501,637 501,860 0,860" fill="url(#redBand)"/>
    </svg>

    <div class="brand-name">KELVO</div>
    <div class="brand-services">ROBOTICS | AUTOMATION | MECHATRONICS<br>PROTOTYPING | SENSING</div>
    <div class="brand-url">kelvolaboratory.com</div>

    <h2 class="section-title expertise-title">
      <span class="light">We are</span> <span class="bold">Specialist</span><br>
      <span class="bold">Design Engineers</span>
    </h2>
    <ul class="bullet-list expertise-list">
      <li>Embedded Electronics and Circuit Design</li>
      <li>Rapid Functional Prototyping</li>
      <li>Sensor and Vision Systems</li>
      <li>Robotics Systems</li>
    </ul>

    <h2 class="section-title projects-title">
      <span class="bold">Our Recent</span> <span class="light">Projects</span>
    </h2>
    <ul class="bullet-list projects-list">
      <li>Robotic concrete sewer probes</li>
      <li>IoT wildlife tracking systems</li>
      <li>Robots for exploring wombat burrows</li>
      <li>Smart pest control technology</li>
    </ul>

    <div class="contact-phone">
      <svg class="phone-icon" viewBox="0 0 24 24" aria-hidden="true">
        <path d="M6.6 3.2l2.4 3.3c.4.5.3 1.2-.1 1.6L7.6 9.4c1 2.4 2.8 4.4 5.1 5.6l1.4-1.2c.5-.4 1.2-.4 1.6 0l3.2 2.5c.5.4.6 1.1.2 1.6l-1.5 2c-.5.6-1.3.9-2 .7C9.6 19 4.6 13.8 3.300 7.8c-.2-.8.1-1.6.8-2l1.9-1.3c.2-.1.4-.2.6-.1z" fill="none" stroke="var(--brand-blue)" stroke-width="1.6" stroke-linejoin="round"/>
        <path d="M14 3.5a7 7 0 0 1 6.5 6.5M14 6.5a4 4 0 0 1 3.5 3.5" fill="none" stroke="var(--brand-blue)" stroke-width="1.6" stroke-linecap="round"/>
      </svg>
      <span class="phone-number">5550-318-274</span>
    </div>
  </div>
</body>
</html>
```